Consumer Facing Energy Data Analytics Startup Needs a Postcard to Promote New Product

We need a set of 2 postcards (6 x 4.25 inches as describers in the attached files) to help us promote our product for a new company based in San Francisco called "Lumo Crest".
We develop an alert platform for customers of energy utility companies. Our initial product is "Lumo Notice" - an application that helps people better manage their energy bill by sending an SMS or email alter in advance of a high bill.
We would like to see designs that use the colors blue and orange (same as in the website: www.lumocrest-demo.com). The text of the postcards will be reworked once a layout has been chosen, but we welcome original ways to attract the customers' attention.
Our goal is ultimately to have our targets go the our website and sign up for our service.
The final deliverable should be 8 vector files (preferable .eps, 4 file types, one version in print and one in web format):
- front of card for our small and medium business customers
- front of card for our residential customers
- back of card for our small and medium business customers
- back of card for our residential customers
- DINPro and Avenir

```html
<!DOCTYPE html>
<html lang="en">
<head>
<meta charset="utf-8">
<title>Lumo Crest Postcards</title>
<link rel="stylesheet" href="https://fonts.googleapis.com/css2?family=Lato:wght@400;700;900&display=swap">
<style>
  :root {
    --blue: #29a3dc;
    --blue-deep: #1a6ea6;
    --blue-light: #3cc0f2;
    --orange: #f8ab3c;
    --orange-deep: #d98a1d;
    --ink: #262626;
    --white: #ffffff;
    --stamp: #e3e3e3;
    --rule: #3a3a3a;
    --pointer: #3a3a3a;
    --backdrop: #5b5b5b;
  }
  * { box-sizing: border-box; margin: 0; padding: 0; }
  html, body {
    width: 904px; height: 1200px; overflow: hidden;
    background: var(--backdrop);
    font-family: "Lato", sans-serif;
  }
  .postcard {
    position: absolute; left: 89px; width: 727px; overflow: hidden;
    background: var(--white);
  }
  .postcard--front { top: 48px; height: 517px; }
  .postcard--back  { top: 624px; height: 515px; }
  .postcard__art { position: absolute; inset: 0; }

  .brand { position: absolute; display: flex; align-items: center; gap: 10px; }
  .brand__dot { width: 40px; height: 40px; border-radius: 50%; background: var(--orange); flex: none; }
  .brand__name {
    font-weight: 700; color: var(--blue); letter-spacing: 2px; font-size: 28px; line-height: 1;
  }
  .brand__tagline {
    font-size: 9.5px; color: var(--blue); letter-spacing: 1px; margin-top: 4px;
  }
  .postcard--front .brand { left: 22px; top: 24px; }
  .postcard--back .brand { left: 430px; top: 360px; flex-direction: column; gap: 8px; text-align: center; }
  .postcard--back .brand__name { font-size: 24px; }

  .headline-box {
    position: absolute; left: 17px; top: 118px; width: 403px; height: 193px;
    border-radius: 12px;
    background: linear-gradient(100deg, var(--blue-deep) 0%, var(--blue) 60%, var(--blue-light) 100%);
    box-shadow: 0 3px 6px rgba(0,0,0,.25);
    padding: 18px 22px;
    color: var(--white); font-weight: 700; text-transform: uppercase;
    font-size: 18.5px; line-height: 1.3;
  }
  .headline-box p + p { margin-top: 14px; }

  .phone-photo {
    position: absolute; left: 12px; top: 300px; width: 200px; height: 217px;
    border-radius: 30px 30px 0 0;
    background: linear-gradient(160deg, #2b2b2b, #111 55%, #c9a58a);
  }

  .cta {
    position: absolute; background: var(--orange); border-radius: 40px;
    text-align: center; color: var(--ink); text-transform: uppercase;
  }
  .cta__main { font-weight: 900; display: block; line-height: 1.05; }
  .cta__sub { font-weight: 700; display: block; line-height: 1.1; }
  .cta::after {
    content: ""; position: absolute; left: 50%; transform: translateX(-50%);
    border-left: 9px solid transparent; border-right: 9px solid transparent;
    border-top-style: solid; border-top-color: var(--pointer);
  }
  .postcard--front .cta { left: 321px; top: 342px; width: 396px; height: 88px; padding-top: 12px; }
  .postcard--front .cta__main { font-size: 30px; }
  .postcard--front .cta__sub { font-size: 21px; margin-top: 4px; }
  .postcard--front .cta::after { bottom: -17px; border-top-width: 18px; }
  .postcard--back .cta { left: 11px; top: 372px; width: 297px; height: 68px; padding-top: 11px; }
  .postcard--back .cta__main { font-size: 23px; }
  .postcard--back .cta__sub { font-size: 16px; margin-top: 2px; }
  .postcard--back .cta::after { bottom: -13px; border-top-width: 14px; }

  .web-address { position: absolute; font-weight: 400; line-height: 1; }
  .postcard--front .web-address { left: 340px; top: 453px; color: var(--white); font-size: 31px; }
  .postcard--back .web-address { left: 26px; top: 460px; color: var(--ink); font-size: 25px; }

  .ribbon {
    position: absolute; left: 7px; top: 184px; width: 296px; height: 87px;
    background: var(--orange); color: var(--white);
    border-radius: 0 0 0 12px;
    padding: 8px 12px; font-size: 18px; line-height: 1.3;
  }
  .ribbon__text { font-weight: 400; }
  .promise {
    position: absolute; left: 14px; top: 282px; width: 272px;
    color: var(--white); font-weight: 700; font-size: 21.5px; line-height: 1.3;
  }

  .stamp { position: absolute; left: 616px; top: 2px; width: 90px; height: 98px; background: var(--stamp); }
  .address-line { position: absolute; left: 363px; width: 342px; height: 2px; background: var(--rule); }
</style>
</head>
<body>

<section class="postcard postcard--front">
  <svg class="postcard__art" width="727" height="517" viewBox="0 0 727 517">
    <path d="M0,350 Q170,335 320,405 Q470,370 727,330 L727,517 L0,517 Z" fill="var(--blue)"/>
    <path d="M0,342 Q170,327 320,397" fill="none" stroke="var(--orange)" stroke-width="8"/>
    <path d="M330,0 Q300,180 380,340" fill="none" stroke="var(--orange)" stroke-width="10"/>
    <path d="M346,0 Q318,180 395,336" fill="none" stroke="var(--blue)" stroke-width="12"/>
    <path d="M362,0 L727,0 L727,325 L405,335 Q336,180 362,0 Z" fill="#c9cfd3"/>
    <path d="M405,335 Q560,340 727,318" fill="none" stroke="var(--orange)" stroke-width="8"/>
  </svg>
  <div role="img" aria-label="Photo of a business team gathered around a laptop in an office"
       style="position:absolute;left:370px;top:0;width:357px;height:320px;background:linear-gradient(135deg,#dfe4e8,#9aa5ad 60%,#6d6a68);clip-path:path('M0,0 L357,0 L357,318 L35,330 Q-30,180 0,0 Z');"></div>

  <div class="brand">
    <span class="brand__dot"></span>
    <div>
      <div class="brand__name">LUMO CREST</div>
      <div class="brand__tagline">ENERGY ANALYTICS AND INSIGHTS</div>
    </div>
  </div>

  <div class="phone-photo" role="img" aria-label="Hand holding a smartphone showing the Lumo Notice bill prediction alert"></div>

  <div class="headline-box">
    <p>Never get the bad surprise of a high energy bill again with Lumo Notice</p>
    <p>Get your alerts on the go by email or SMS so you’re always in control</p>
  </div>

  <div class="cta">
    <span class="cta__main">Visit our website</span>
    <span class="cta__sub">and sign up for our service</span>
  </div>
  <div class="web-address">www.lumocrest-demo.com</div>
</section>

<section class="postcard postcard--back">
  <svg class="postcard__art" width="727" height="515" viewBox="0 0 727 515">
    <rect width="727" height="515" fill="var(--blue)"/>
    <path d="M358,0 L727,0 L727,420 Q620,470 480,478 Q320,460 304,320 Q296,160 358,0 Z" fill="var(--white)"/>
    <path d="M350,0 Q288,160 296,320 Q314,468 480,486" fill="none" stroke="var(--orange)" stroke-width="10"/>
    <path d="M480,488 Q620,480 727,430" fill="none" stroke="var(--orange)" stroke-width="12"/>
    <path d="M301,184 L329,169 L329,283 L301,297 Z" fill="var(--orange-deep)"/>
  </svg>
  <div role="img" aria-label="Photo of a woman sitting by a bright window using a laptop"
       style="position:absolute;left:0;top:0;width:345px;height:190px;background:linear-gradient(120deg,#e9e7e3,#bcd3e6 55%,#8fb6dc);clip-path:path('M0,0 L345,0 Q315,100 305,190 L0,190 Z');"></div>

  <div class="stamp"></div>
  <div class="address-line" style="top:206px"></div>
  <div class="address-line" style="top:242px"></div>
  <div class="address-line" style="top:282px"></div>

  <div class="ribbon"><p class="ribbon__text">Save on your energy expenses with our simple and easy timely recommendations.</p></div>
  <p class="promise">Our email alerts will put you in control of your energy usage</p>

  <div class="cta">
    <span class="cta__main">Visit our website</span>
    <span class="cta__sub">and sign up for our service</span>
  </div>
  <div class="web-address">www.lumocrest-demo.com</div>

  <div class="brand">
    <span class="brand__dot"></span>
    <div>
      <div class="brand__name">LUMO CREST</div>
      <div class="brand__tagline">ENERGY ANALYTICS AND INSIGHTS</div>
    </div>
  </div>
</section>

</body>
</html>
```